tiling company needs letterhead urgent

We need a logo to represent our company on an electronic letterhead. We are a tiling firm called Corwell Tiling Ltd and undertake all aspects of tiling work. The final design of the logo should incorporate the type of work we do and should be modern. We do not want any designs which may be considered 'novelty' or 'cartoonish.' No characters please, we require something sleek and contemporary . Please ensure the company name is central to your design ,Corwell Tiling Ltd

Industry/Entity Type

Electronic

Requirements
Must have
• text on letterhead to included

Registered address 41 Birch lane Failsworth Manchester M359QT
Company number 5267093
VAT no 412957386
Mobile no 07831659047
Office no 0161 574 8192
Web :www.floorvane.co.uk
Email : gareth@floorvane.co.uk
Nice to have
• a tile theme

```html
<!DOCTYPE html>
<html lang="en">
<head>
<meta charset="utf-8">
<title>Corwell Tiling Ltd — Letterhead</title>
<link rel="stylesheet" href="https://fonts.googleapis.com/css2?family=Open+Sans:wdth,wght@75..100,400;75..100,700&display=swap">
<style>
  :root {
    --brand-red: #d4202f;
    --brand-grey: #4b4b4d;
    --rule-grey: #b9b9bb;
    --soft-grey: #e4e4e7;
    --footer-grey: #555558;
    --paper: #ffffff;
  }
  * { margin: 0; padding: 0; box-sizing: border-box; }
  html, body {
    width: 849px;
    height: 1200px;
    overflow: hidden;
    background: var(--paper);
  }
  .letterhead {
    position: relative;
    width: 849px;
    height: 1200px;
    background: var(--paper);
    font-family: "Open Sans", Arial, sans-serif;
  }
  .page-shapes {
    position: absolute;
    inset: 0;
    width: 849px;
    height: 1200px;
  }
  .brand {
    position: absolute;
    left: 196px;
    top: 66px;
    display: flex;
    align-items: center;
    gap: 14px;
  }
  .brand-square {
    width: 56px;
    height: 56px;
    background: var(--brand-red);
  }
  .brand-name {
    font-weight: 700;
    font-size: 42px;
    letter-spacing: -0.5px;
    color: var(--brand-grey);
    line-height: 1;
    white-space: nowrap;
  }
  .contact-footer {
    position: absolute;
    left: 80px;
    top: 1080px;
    font-stretch: 75%;
    font-size: 13px;
    letter-spacing: 1.1px;
    color: var(--footer-grey);
    line-height: 20px;
    white-space: nowrap;
  }
  .contact-label {
    color: var(--brand-red);
    font-weight: 700;
  }
  .contact-sep {
    color: var(--brand-red);
    font-weight: 700;
    margin: 0 3px;
  }
  .contact-vat {
    font-size: 15px;
    letter-spacing: 0.8px;
  }
</style>
</head>
<body>
<main class="letterhead">
  <svg class="page-shapes" viewBox="0 0 849 1200" aria-hidden="true">
    <line class="header-rule" x1="268" y1="111" x2="815" y2="111" stroke="var(--rule-grey)" stroke-width="1.2"/>
    <polygon class="corner-top-right" points="849,68 815,111 849,154" fill="var(--brand-red)"/>
    <polygon class="tile-accent-grey" points="0,1007 146,1007 55,1084" fill="var(--soft-grey)"/>
    <polygon class="corner-bottom-left" points="0,1067 51,1130 0,1193" fill="var(--brand-red)"/>
    <polygon class="corner-bottom-right" points="849,1069 799,1130 849,1193" fill="var(--brand-red)"/>
  </svg>

  <header class="brand">
    <span class="brand-square"></span>
    <h1 class="brand-name">CORWELL TILING LTD</h1>
  </header>

  <footer class="contact-footer">
    <p class="contact-line">41 Birch lane Failsworth Manchester M359QT<span class="contact-sep">•</span><span class="contact-label">Mob:</span> 07831659047<span class="contact-sep">•</span><span class="contact-label">Off:</span> 0161 574 8192</p>
    <p class="contact-line"><span class="contact-label">Web:</span> www.floorvane.co.uk<span class="contact-sep">•</span><span class="contact-label">Email:</span> gareth@floorvane.co.uk<span class="contact-sep">•</span>Company number 5267093<span class="contact-sep">•</span><span class="contact-vat">VAT no 412957386</span></p>
  </footer>
</main>
</body>
</html>
```